Korvane Sky Works, LLC - Business Card

I currently have a drone business that specializes in aerial photography, thermal image inspections, deer recovery, search and rescue, custom agricultural applications. i will attach my current business card as well as some logos to incorporate for a new up to date business card
Updates

Designs look the same

Sick

Target Market(s)

farmers, hunters

Contact Information for Business Card

name address phone number (as existing card i attached)

Requirements
Must have
• im good with existing business card, but would like an agricultural twist

```html
<!DOCTYPE html>
<html lang="en">
<head>
<meta charset="utf-8">
<title>Korvane Sky Works, LLC – Business Card</title>
<link rel="stylesheet" href="https://fonts.googleapis.com/css2?family=Oswald:wght@600&family=Lato:wght@400;700&display=swap">
<style>
  :root {
    --stage: #8e8e8e;
    --card-light: #ffffff;
    --card-dark: #1f1f1f;
    --ink: #1b1b1b;
    --text-grey: #3a3a3a;
    --white: #ffffff;
    --green: #4a9a1c;
    --red: #ff0a0a;
    --label: #1e1e1e;
  }
  * { box-sizing: border-box; margin: 0; padding: 0; }
  html, body { width: 1200px; height: 761px; overflow: hidden; }
  body {
    position: relative;
    background: var(--stage);
    font-family: "Lato", Arial, sans-serif;
  }
  .card {
    position: absolute;
    width: 407px;
    height: 232px;
    border-radius: 12px;
    overflow: hidden;
  }
  .card--front { background: var(--card-light); top: 124px; }
  .card--back  { background: var(--card-dark);  top: 406px; }
  .set-green { left: 158px; --accent: var(--green); }
  .set-red   { left: 636px; --accent: var(--red); }

  /* brand name in place of the mark */
  .brand {
    position: absolute;
    left: 0; right: 0;
    display: flex;
    align-items: center;
    justify-content: center;
    gap: 10px;
    font-family: "Oswald", Arial, sans-serif;
    font-weight: 600;
    color: var(--accent);
    letter-spacing: 1px;
    text-transform: uppercase;
  }
  .brand__dot {
    width: 16px; height: 16px;
    border-radius: 50%;
    background: var(--accent);
  }
  .card--front .brand { top: 36px; font-size: 40px; line-height: 1; }
  .card--back .brand { top: 72px; font-size: 48px; line-height: 1; }

  /* person */
  .person {
    position: absolute;
    left: 20px;
    top: 136px;
    width: 157px;
    text-align: right;
  }
  .person__name {
    font-family: "Oswald", Arial, sans-serif;
    font-weight: 600;
    font-size: 25px;
    line-height: 1;
    color: var(--accent);
    letter-spacing: 0.3px;
    white-space: nowrap;
  }
  .person__role {
    font-size: 11px;
    color: var(--ink);
    margin-top: 1px;
  }
  .divider {
    position: absolute;
    left: 195px; top: 125px;
    width: 1.5px; height: 69px;
    background: var(--accent);
  }

  /* contact list */
  .contact {
    position: absolute;
    left: 207px; top: 122px;
    list-style: none;
    font-size: 9.6px;
    color: var(--text-grey);
  }
  .contact li {
    display: flex;
    align-items: flex-start;
    gap: 8px;
    line-height: 14px;
  }
  .contact li + li { margin-top: 0.5px; }
  .contact .gap { margin-top: 3px; }
  .contact svg { width: 9px; height: 9px; flex: none; margin-top: 2.5px; fill: var(--accent); }
  .contact .company { color: var(--accent); font-weight: 700; }
  .contact .indent { padding-left: 17px; }

  /* bottom band */
  .band {
    position: absolute;
    left: 0; right: 0; bottom: 0;
    height: 8px;
    background: var(--ink);
  }
  .band__accent {
    position: absolute;
    left: 0; top: 0; bottom: 0;
    width: 273px;
    background: var(--accent);
    clip-path: polygon(0 0, 100% 0, calc(100% - 6px) 100%, 0 100%);
  }
  .band__gap {
    position: absolute;
    left: 270px; top: 0; bottom: 0;
    width: 6px;
    background: var(--card-light);
    clip-path: polygon(4px 0, 6px 0, 2px 100%, 0 100%);
  }

  /* services on back */
  .services {
    position: absolute;
    left: 0; right: 0; top: 187px;
    text-align: center;
    color: var(--white);
    font-size: 9.6px;
    line-height: 14px;
    text-transform: uppercase;
    letter-spacing: 0.1px;
  }
  .services .sep { color: var(--accent); }

  .set-label {
    position: absolute;
    top: 668px;
    width: 407px;
    text-align: center;
    font-size: 16px;
    letter-spacing: 2.5px;
    color: var(--label);
  }
</style>
</head>
<body>

<svg width="0" height="0" style="position:absolute" aria-hidden="true">
  <defs>
    <symbol id="icon-pin" viewBox="0 0 10 10"><path d="M5 0a3.6 3.6 0 0 0-3.6 3.6C1.4 6.2 5 10 5 10s3.6-3.8 3.6-6.4A3.6 3.6 0 0 0 5 0zm0 5a1.4 1.4 0 1 1 0-2.8A1.4 1.4 0 0 1 5 5z"/></symbol>
    <symbol id="icon-phone" viewBox="0 0 10 10"><path d="M2.1 0.4 3.6 2c.3.3.3.8 0 1.1l-.7.7c.6 1.3 1.8 2.5 3.2 3.2l.7-.7c.3-.3.8-.3 1.1 0l1.6 1.5c.3.3.3.8 0 1.1l-.8.8C7.6 10.6 0 4.4.3 1.4l.7-1c.3-.3.8-.3 1.1 0z"/></symbol>
    <symbol id="icon-mail" viewBox="0 0 10 10"><path d="M0 1.8h10v6.4H0z M0.6 2.3 5 5.6l4.4-3.3" stroke="#fff" stroke-width="0.8"/></symbol>
    <symbol id="icon-globe" viewBox="0 0 10 10"><circle cx="5" cy="5" r="5"/><path d="M2 2.5c1 .3 1.6 1 1.3 2-.3.8.7 1.2.6 2.2 0 .8.5 1.4 1 1.8M6.5 1.2c-.3.8.2 1.5 1 1.6.8.2 1.2 1 .8 1.8" stroke="#fff" stroke-width="0.8" fill="none"/></symbol>
  </defs>
</svg>

<!-- Set 01 : green -->
<section class="card card--front set-green">
  <div class="brand"><span class="brand__dot"></span>Korvane</div>
  <div class="person">
    <p class="person__name">DALTON REYES</p>
    <p class="person__role">Owner</p>
  </div>
  <div class="divider"></div>
  <ul class="contact">
    <li><svg><use href="#icon-pin"/></svg><span class="company">Korvane Sky Works, LLC</span></li>
    <li class="indent">214 W. Elm St. Harlow, OH 45390</li>
    <li class="gap"><svg><use href="#icon-phone"/></svg>419-555-0142</li>
    <li><svg><use href="#icon-mail"/></svg>korvanesky@mail.com</li>
    <li><svg><use href="#icon-globe"/></svg>korvaneskyworks.com</li>
  </ul>
  <div class="band"><div class="band__accent"></div><div class="band__gap"></div></div>
</section>

<section class="card card--back set-green">
  <div class="brand"><span class="brand__dot"></span>Korvane</div>
  <p class="services">
    Thermal Image Inspections <span class="sep">&bull;</span> Deer Recovery<br>
    Search and Rescue <span class="sep">&bull;</span> Real Estate Photography
  </p>
</section>

<p class="set-label" style="left:158px">FRONT &amp; BACK 01</p>

<!-- Set 02 : red -->
<section class="card card--front set-red">
  <div class="brand"><span class="brand__dot"></span>Korvane</div>
  <div class="person">
    <p class="person__name">DALTON REYES</p>
    <p class="person__role">Owner</p>
  </div>
  <div class="divider"></div>
  <ul class="contact">
    <li><svg><use href="#icon-pin"/></svg><span class="company">Korvane Sky Works, LLC</span></li>
    <li class="indent">214 W. Elm St. Harlow, OH 45390</li>
    <li class="gap"><svg><use href="#icon-phone"/></svg>419-555-0142</li>
    <li><svg><use href="#icon-mail"/></svg>korvanesky@mail.com</li>
    <li><svg><use href="#icon-globe"/></svg>korvaneskyworks.com</li>
  </ul>
  <div class="band"><div class="band__accent"></div><div class="band__gap"></div></div>
</section>

<section class="card card--back set-red">
  <div class="brand"><span class="brand__dot"></span>Korvane</div>
  <p class="services">
    Thermal Image Inspections <span class="sep">&bull;</span> Deer Recovery<br>
    Search and Rescue <span class="sep">&bull;</span> Real Estate Photography
  </p>
</section>

<p class="set-label" style="left:636px">FRONT &amp; BACK 02</p>

</body>
</html>
```